Packaging design pot 500gr Polynesian honey

Task Description

Concept of design:

"This Polynesian island is a small piece of paradise nestled in the South Pacific, away from any form of civilization ( ideal place for producing honey of excellence )
= Images / symbols that induces dreaming)); (100% organic, 100% natural organic Honey logo)
Elegant, subtle , eyes catching, NO pictures of bees , Simple colors: BLACK, GOLD, WHITE, tranparency . (Designer discretion)
(Bio label optional )

the Labels: Hex1 product of TAHITI header: VELINOA HONEY (brand name) MAY USE all images herein below , free of copyright (Macro coconut flower, coconut white sand beach, exoticism; 500 gr; text on back (see attached text); Position the bar code vertically on the back; Mandatory address: Website on the back, infocontact, registration number.

500g pot :
HEIGHT With cap 12.00cm Without cap 11.85 cm
outside diameter 7.24cm
Label height should only be = 5, 1 cm x height
See the container with black cap.

Deadline
March 15, 2018 ( postpone if needed )
Updates

To all participants, i have added a personal photo you may want to consider in your creative process. If the upper section of the photo is exploited, I thought it has something interesting to bring: blue sky on the background including a shadow ot the coconut leaves, ( no bees please).

Finally i have added the colour of Velinoa Honey

Dear participants, I have updated two files to be taken into account onward : 1) final text: in French ; the replicate is English for the English version valid with the identical Graphic design 2) the true colours of Velinoa Honey, for your consideration. I thought that with the help of day light i could enhance its true body colour. Best regards, Mr KOR

Target Market(s)

Target the Asian market , Onward The US MARKET, (LUXURY oriented)

Font styles to use
Serif

Colors

Designer to choose colors to be used in the design.

Requirements
Must have
• Website address on the back, infocontact, registration number,
• texte ( summary )
• coconut tree honey ( ORIGIN )
• Color code : BLACK , GOLD , light , transparency
• COLORS THAT MATCH COLOR OF THE HONEY : DARK RED AMBER SEE IMAGE ATTACHED
Nice to have
• A matching logo
• A 400g Squezze bottle format ;
• h18.5*d7.8*c3.2(cm)
Should not have
• No Bees

```html
<!DOCTYPE html>
<html lang="fr">
<head>
<meta charset="utf-8">
<title>Velinoa Honey — Étiquette 500 gr</title>
<link rel="stylesheet" href="https://fonts.googleapis.com/css2?family=Playfair+Display:wght@900&family=Rokkitt:wght@400;600&family=Roboto+Condensed:wght@400;500&display=swap">
<style>
  :root {
    --page: #ffffff;
    --ink: #111111;
    --badge: #151515;
    --paper: #f4f4f2;
    --rule: #e9e9e6;
    --sky: #9fd3e0;
    --sea: #6fb9c4;
    --palm: #8fae3a;
    --sand: #e6ddcc;
    --husk: #c9862b;
    --husk-dark: #6b4526;
    --husk-light: #e7b24d;
  }
  html, body {
    margin: 0;
    width: 1200px;
    height: 1200px;
    overflow: hidden;
    background: var(--page);
  }
  .label-art {
    display: block;
    width: 1200px;
    height: 1200px;
  }
  .arc-title {
    font-family: "Rokkitt", Georgia, serif;
    font-weight: 600;
    font-size: 62px;
    letter-spacing: 16px;
    fill: var(--paper);
  }
  .purity {
    font-family: "Roboto Condensed", Arial, sans-serif;
    font-weight: 500;
    fill: var(--paper);
  }
  .brand-name {
    font-family: "Playfair Display", Georgia, serif;
    font-weight: 900;
    font-size: 84px;
    fill: var(--paper);
  }
  .organic {
    font-family: "Rokkitt", Georgia, serif;
    font-weight: 400;
    font-size: 34px;
    letter-spacing: 6px;
    fill: var(--paper);
  }
  .weight {
    font-family: "Roboto Condensed", Arial, sans-serif;
    font-weight: 400;
    font-size: 36px;
    fill: var(--paper);
  }
</style>
</head>
<body>
<svg class="label-art" viewBox="0 0 1200 1200" xmlns="http://www.w3.org/2000/svg">
  <defs>
    <linearGradient id="beach-tones" x1="0" y1="0" x2="0" y2="1">
      <stop offset="0" stop-color="var(--palm)"/>
      <stop offset="0.35" stop-color="var(--sky)"/>
      <stop offset="0.6" stop-color="var(--sea)"/>
      <stop offset="0.75" stop-color="var(--sand)"/>
      <stop offset="1" stop-color="var(--sand)"/>
    </linearGradient>
    <linearGradient id="flower-tones" x1="0" y1="0" x2="1" y2="1">
      <stop offset="0" stop-color="var(--husk-dark)"/>
      <stop offset="0.45" stop-color="var(--husk)"/>
      <stop offset="0.8" stop-color="var(--husk-light)"/>
      <stop offset="1" stop-color="var(--husk-dark)"/>
    </linearGradient>
    <linearGradient id="badge-fade" x1="0" y1="0" x2="0" y2="1">
      <stop offset="0" stop-color="var(--badge)" stop-opacity="0.96"/>
      <stop offset="0.62" stop-color="var(--badge)" stop-opacity="0.94"/>
      <stop offset="0.7" stop-color="#5a5a5a" stop-opacity="0.6"/>
      <stop offset="1" stop-color="#4a4a4a" stop-opacity="0.55"/>
    </linearGradient>
    <path id="arc-top" d="M 395 600 A 205 205 0 0 1 805 600"/>
    <path id="arc-bottom" d="M 372 600 A 228 228 0 0 0 828 600"/>
  </defs>

  <!-- photo band -->
  <rect class="photo-beach" x="50" y="545" width="560" height="272" fill="url(#beach-tones)" role="img" aria-label="Palm leaves over a white sand beach and turquoise lagoon"/>
  <rect class="photo-flower" x="590" y="545" width="560" height="272" fill="url(#flower-tones)" role="img" aria-label="Close-up of an opening coconut flower husk"/>

  <!-- black stripes -->
  <g class="stripe stripe-top">
    <rect x="50" y="545" width="1100" height="44" fill="var(--ink)"/>
    <rect x="50" y="556" width="1100" height="3" fill="var(--rule)"/>
    <rect x="50" y="574" width="1100" height="5" fill="var(--rule)"/>
  </g>
  <g class="stripe stripe-bottom">
    <rect x="50" y="773" width="1100" height="44" fill="var(--ink)"/>
    <rect x="50" y="783" width="1100" height="5" fill="var(--rule)"/>
    <rect x="50" y="802" width="1100" height="3" fill="var(--rule)"/>
  </g>

  <!-- central badge -->
  <g class="badge">
    <circle cx="600" cy="600" r="242" fill="url(#badge-fade)"/>
    <circle cx="600" cy="600" r="242" fill="none" stroke="var(--ink)" stroke-width="6"/>

    <text class="arc-title"><textPath href="#arc-top" startOffset="50%" text-anchor="middle">TAHITI</textPath></text>

    <text class="purity" x="600" y="452" text-anchor="middle" font-size="38">100%</text>
    <text class="purity" x="600" y="482" text-anchor="middle" font-size="18" letter-spacing="1">★★★  NATUREL  ★★★</text>

    <text class="brand-name" x="600" y="577" text-anchor="middle">VELINOA</text>
    <text class="brand-name" x="600" y="650" text-anchor="middle">HONEY</text>

    <rect x="455" y="664" width="290" height="3" fill="var(--paper)"/>
    <text class="organic" x="600" y="697" text-anchor="middle">100% BIO</text>
    <rect x="455" y="706" width="290" height="3" fill="var(--paper)"/>

    <text class="weight" x="600" y="742" text-anchor="middle">500 gr</text>

    <text class="arc-title" dy="-6"><textPath href="#arc-bottom" startOffset="50%" text-anchor="middle">MIEL</textPath></text>
  </g>
</svg>
</body>
</html>
```